Design for Brochure

We need a graphic design template for an investment brochure. The brochure will have information about the firm, about the investment philosophy and about the performance of the model. We'd like it to match up with our logo and business card designs.
Check out the website for content for now. We are most interested in the layout and template aspect. of the brochure.
We'd like to have a map or something showing locations.
Updates
Logo files and font files uploaded to design brief. Take a look at our website and see what you can build out from the info located there. www.bluefernwealth.com
I'd say for content use the following pages off our website:
Target Market(s)
Investors and investment advisors
Industry/Entity Type
Graphic Design
Font styles to use
Other font styles liked:
- It's uploaded in the files section
Requirements
Must have
- Logo Integration and like design to our business cards.
Also need it in publisher and word formats.
Multi page brochure.

```html
<!DOCTYPE html>
<html lang="en">
<head>
<meta charset="utf-8">
<title>Bluefern Advisors Brochure</title>
<link href="https://fonts.googleapis.com/css2?family=Lato:wght@400;700&family=Open+Sans:wght@400;600&display=swap" rel="stylesheet">
<style>
  :root {
    --brand-green: #8cc540;
    --charcoal: #4a4a4c;
    --dark-band: #505052;
    --ink: #444446;
    --paper: #ffffff;
    --mist: #f2f2f2;
    --rule: #c8c8c8;
  }
  * { margin: 0; padding: 0; box-sizing: border-box; }
  html, body { width: 1200px; height: 800px; overflow: hidden; background: var(--paper); }
  .spread { position: relative; width: 1200px; height: 800px; overflow: hidden;
    font-family: "Lato", sans-serif; color: var(--ink);
    background: radial-gradient(ellipse at 60% 70%, var(--paper) 0%, var(--mist) 70%, #ebebeb 100%); }

  .back-cover-panel { position: absolute; left: 0; top: 0; width: 605px; height: 428px; background: var(--brand-green); overflow: hidden; }
  .back-cover-panel .faint-name { position: absolute; left: 40px; top: 250px; font-family: "Lato", sans-serif;
    font-size: 62px; line-height: 1; font-weight: 400; color: rgba(0,0,0,0.06); letter-spacing: 3px; white-space: nowrap;
    transform: rotate(-25deg); transform-origin: left bottom; }

  .front-cover-head { position: absolute; left: 605px; top: 0; width: 595px; height: 239px; background: var(--paper);
    display: flex; align-items: center; justify-content: center; }
  .brand-name { font-family: "Lato", sans-serif; font-weight: 400; color: var(--charcoal); white-space: nowrap; }
  .front-cover-head .brand-name { font-size: 42px; letter-spacing: 3px; margin-top: 10px; }

  .accent-rule { position: absolute; left: 605px; top: 239px; width: 595px; height: 7px; background: var(--brand-green); }

  .photo-strip { position: absolute; top: 251px; height: 130px; }
  .photo-pen { left: 605px; width: 205px; background: linear-gradient(135deg, #e8eef4 0%, #b9c7d6 55%, #5d6a7a 100%); }
  .photo-sail { left: 810px; width: 233px; background: linear-gradient(90deg, #8a6a45 0%, #b3894f 30%, #4f8fd0 60%, #2f6fae 100%); }
  .photo-bull { left: 1043px; width: 157px; background: linear-gradient(135deg, #d6d6d6 0%, #8c8c8c 50%, #3e3e3e 100%); }

  .service-band { position: absolute; left: 605px; top: 381px; width: 595px; height: 47px; }
  .service-band svg { position: absolute; left: 0; top: 0; }
  .service-label { position: absolute; top: 14px; font-family: "Open Sans", sans-serif; font-weight: 600;
    font-size: 16px; color: var(--paper); white-space: nowrap; letter-spacing: -0.2px; }

  .contact-logo { position: absolute; left: 60px; top: 572px; }
  .contact-logo .brand-name { font-size: 23px; letter-spacing: 1px; }
  .contact-divider { position: absolute; left: 293px; top: 523px; width: 1px; height: 145px; background: var(--rule); }
  .contact-list { position: absolute; left: 311px; top: 530px; list-style: none; font-size: 14px; line-height: 19px; color: var(--ink); }
  .contact-list li { display: flex; align-items: flex-start; gap: 6px; }
  .contact-list li svg { flex: none; margin-top: 4px; }
  .contact-list .address { margin-bottom: 9px; }

  .web-tab { position: absolute; top: 752px; height: 48px; }
  .web-tab svg { position: absolute; left: 0; top: 0; }
  .web-address { position: absolute; top: 13px; font-size: 17px; color: var(--paper); letter-spacing: 0.5px; white-space: nowrap; }
  .web-address b { font-weight: 700; }
</style>
</head>
<body>
<main class="spread">

  <section class="back-cover-panel">
    <span class="faint-name">Bluefern Advisors</span>
  </section>

  <header class="front-cover-head">
    <span class="brand-name">Bluefern Advisors</span>
  </header>
  <div class="accent-rule"></div>

  <div class="photo-strip photo-pen" role="img" aria-label="Photo of a fountain pen resting on signed papers"></div>
  <div class="photo-strip photo-sail" role="img" aria-label="Photo of coins blended with a sailboat bow on open blue water"></div>
  <div class="photo-strip photo-bull" role="img" aria-label="Black and white photo of a bronze bull statue on a city street"></div>

  <div class="service-band">
    <svg width="595" height="47" viewBox="0 0 595 47">
      <polygon points="0,0 595,0 595,0 552,47 0,47" fill="var(--dark-band)"/>
      <polygon points="545,47 595,0 595,47" fill="var(--brand-green)"/>
    </svg>
    <span class="service-label" style="left:12px">ASSET MANAGEMENT</span>
    <span class="service-label" style="left:192px">FINANCIAL PLANNING</span>
    <span class="service-label" style="left:373px">CASH MANAGEMENT</span>
  </div>

  <div class="contact-logo"><span class="brand-name">Bluefern Advisors</span></div>
  <div class="contact-divider"></div>
  <ul class="contact-list">
    <li class="address">
      <svg width="11" height="15" viewBox="0 0 11 15"><path d="M5.5 0C2.5 0 0 2.4 0 5.4 0 9.3 5.5 15 5.5 15S11 9.3 11 5.4C11 2.4 8.5 0 5.5 0z" fill="var(--brand-green)"/><circle cx="5.5" cy="5.3" r="2" fill="#fff"/></svg>
      <span>482 Harbor Lane, San<br>Ca 94110, United States</span>
    </li>
    <li>
      <svg width="12" height="10" viewBox="0 0 12 10"><path d="M0 3C0 1 3 0 6 0s6 1 6 3v1H9V2.5H3V4H0z" fill="var(--brand-green)"/><rect x="2" y="5" width="8" height="5" rx="1" fill="var(--brand-green)"/></svg>
      <span>000 000 0000</span>
    </li>
    <li>
      <svg width="12" height="12" viewBox="0 0 12 12"><rect x="2.5" y="0" width="7" height="12" rx="1.5" fill="var(--brand-green)"/><rect x="3.8" y="1.5" width="4.4" height="7.5" fill="#fff"/></svg>
      <span>000 000 0000</span>
    </li>
    <li>
      <svg width="12" height="10" viewBox="0 0 12 10"><rect x="3" y="0" width="6" height="3" fill="var(--brand-green)"/><rect x="0" y="3.5" width="12" height="5" rx="1" fill="var(--brand-green)"/></svg>
      <span>000 000 0000</span>
    </li>
    <li>
      <svg width="12" height="9" viewBox="0 0 12 9"><rect x="0" y="0" width="12" height="9" fill="var(--brand-green)"/><path d="M0 0l6 5 6-5" stroke="#fff" stroke-width="1.2" fill="none"/></svg>
      <span>hello@bluefernwealth.com</span>
    </li>
  </ul>

  <div class="web-tab" style="left:0;width:290px">
    <svg width="290" height="48" viewBox="0 0 290 48"><polygon points="0,0 245,0 290,48 0,48" fill="var(--dark-band)"/></svg>
    <span class="web-address" style="left:16px">www.<b>bluefernwealth</b>.com</span>
  </div>

  <div class="web-tab" style="left:603px;width:597px">
    <svg width="597" height="48" viewBox="0 0 597 48">
      <polygon points="0,17 323,17 306,48 0,48" fill="var(--brand-green)"/>
      <polygon points="342,48 383,0 597,0 597,48" fill="var(--dark-band)"/>
    </svg>
    <span class="web-address" style="left:362px">www.<b>bluefernwealth</b>.com</span>
  </div>

</main>
</body>
</html>
```